Book Cover for a book on Lantern Road Ventures

I am self-publishing my book on Brindlemark and need a book cover made. Below are the details. See attached templates for size we need to use. I also attached a previous cover we had made that I liked. The problem with it was they were two boys helping each other but the book is about women. I'm open to your ideas on the cover though, but I wanted to show you a style I liked as an idea.
Front of Cover
Book Title: Lantern Road Ventures
Book Subtitle: Loose Pages of a Harbor Keeper
Author Name: Mirela T. Dunbar
Add on the Spine of Cover: Lantern Road Ventures and Mirela T. Dunbar
Back of the Cover Text:
Lantern Road Ventures: Loose Pages of a Harbor Keeper is an honest account of a business owner’s experience attempting to navigate the start-up community while also pursuing spiritual growth. Author Mirela Dunbar defines a spiritual entrepreneur as “someone who runs an enterprise with the purpose of growing love rather than material gain.” This book discusses the three dimensions of Lantern Road Ventures:
1. The business is an integral part of the founder’s spiritual journey.
2. Employees working for the spiritual enterprise, whether they know it or not, encounter this company because it's part of their spiritual path.
3. The business itself has a life force of its own and its purpose is to further the kingdom of heaven on earth.
These three dimensions happen simultaneously and work together to produce the greatest possible result. However, this can feel confusing to a founder juggling these dimensions while also trying to manage and run a business. This is not a formulaic self-help book or roadmap. Rather, it is a compilation of personal reflections that often seem at odds with the traditional world of entrepreneurship.
Below the description add my picture (see attached for my picture)
Bio text:
Mirela Dunbar founded Calveta with the vision of ushering in a life-long education system that shifts away from standardization to one that empowers people to live their purpose. In college, Mirela interned for Open Kettle, a women’s empowerment initiative where she recognized her passion for helping people find their voice. Mirela's 20-year journey has come full circle to empowering other female CEOs who are pursuing the path of Lantern Road Ventures.
NOTE: Please note that Brindlemark puts a bar code on the bottom right of the back cover as is noted on the attached template.
Size template is attached to the brief, here are the sizes typed out:
# Description Width (in) Height (in)
1 Full Cover 12.79 9.25
2 Front Cover 6 9
3 Safe Area 5.875 8.75
4 Bleed 0.125 0.125
5 Margin 0.125 0.125
6 Spine 0.54 9
7 Spine Safe Area 0.415 8.75
8 Spine Margin 0.062 0.062
9 Barcode Margin 0.25 0.25
Pre-publication checklist
BRINDLEMARK TIPS for the final cover:
1. Save as a PDF. Your cover must be a single PDF that includes the back cover, spine, and front cover as one image.
2. Flatten all transparencies. These can cause the file to print with missing or distorted content. Consult your software's documentation to learn how.
3. Embed your fonts. Consult your software's documentation to learn how.
4. Remove crop marks, color bars, template text. Crop marks are lines showing where pages should be trimmed. Color bars are strips with a series of patches used to ensure color balance during printing. Also, remove any template text, PDF creation guides, or software references.
5. Ensure your cover image meets the minimum resolution of 300 DPI (dots per inch).
6. Optimize PDFs. Optimization is useful to reduce your file size, allowing for higher performance when transferring, uploading, viewing, and printing the files.
7. Remove file security. Locked or encrypted files will fail review.
Target Market(s)
Women who want to be CEOs or are currently CEOs of companies.
Industry/Entity Type
Entrepreneurship, business, spirituality
Requirements
Must have
- Just the text on the description. A very welcoming feel.
Nice to have
- I like the idea of having a sunrise/sunset in the image somehow like in the example I attached to the brief, but again I'm open.
Should not have
- Please don't put any yoga or meditation poses or hands outstretched. I have a lot of interesting ones that look like my example so if you are going to submit after Saturday 10/29, please only do so if you have a new idea! Thanks!

```html
<!DOCTYPE html>
<html lang="en">
<head>
<meta charset="utf-8">
<title>Lantern Road Ventures — Full Cover</title>
<link rel="stylesheet" href="https://fonts.googleapis.com/css2?family=Italianno&family=Cormorant+Garamond:wght@500;600&family=Montserrat:wght@500;600&family=Open+Sans:wght@400;600&display=swap">
<style>
  :root {
    --page: #f1f1f1;
    --night: #141c2e;
    --night-deep: #0c1322;
    --dusk: #2a3550;
    --ember: #e8702c;
    --ember-soft: #f4a15c;
    --glow: #ffd8a8;
    --ink-light: #f3efe9;
    --ink-muted: #c9ccd6;
    --paper: #ffffff;
  }
  * { box-sizing: border-box; margin: 0; padding: 0; }
  html, body { width: 847px; height: 1200px; overflow: hidden; background: var(--page); }
  .canvas { position: relative; width: 847px; height: 1200px; }

  .full-cover {
    position: absolute; left: 20px; top: 308px; width: 807px; height: 584px;
    display: grid; grid-template-columns: 386px 34px 387px;
    background: var(--night); overflow: hidden;
    box-shadow: 0 6px 20px rgba(0,0,0,.18);
  }
  .sunset-art {
    position: absolute; inset: 0;
    background:
      radial-gradient(ellipse 90px 70px at 470px 130px, rgba(255,230,190,.95), rgba(255,170,90,.55) 45%, rgba(232,112,44,0) 100%),
      radial-gradient(ellipse 260px 200px at 480px 170px, rgba(232,112,44,.55), rgba(120,60,60,.25) 55%, rgba(20,28,46,0) 100%),
      radial-gradient(ellipse 300px 260px at 560px 420px, rgba(60,75,110,.45), rgba(20,28,46,0) 100%),
      linear-gradient(180deg, var(--dusk) 0%, var(--night) 45%, var(--night-deep) 100%);
  }

  .back-cover, .spine, .front-cover { position: relative; }

  .back-cover { padding: 40px 26px 30px 28px; color: var(--ink-light); font-family: "Open Sans", sans-serif; }
  .back-copy { font-size: 7.4px; line-height: 1.5; }
  .back-copy p { margin-bottom: 6px; }
  .back-copy ol { list-style: none; margin: 0 0 6px 8px; }
  .back-copy li { margin-bottom: 4px; }
  .author-block { position: absolute; left: 28px; top: 452px; width: 220px; display: flex; gap: 10px; }
  .author-photo { flex: 0 0 52px; height: 60px; background: linear-gradient(160deg, #a06a5a, #5a3a3e 60%, #2c2630); }
  .author-bio { font-size: 6.4px; line-height: 1.45; color: var(--ink-muted); }
  .barcode-area { position: absolute; right: 28px; bottom: 28px; width: 62px; height: 58px; background: var(--paper); }

  .spine {
    display: flex; flex-direction: column; align-items: center; justify-content: space-between;
    padding: 22px 0 28px; border-left: 1px solid rgba(255,255,255,.08); border-right: 1px solid rgba(255,255,255,.08);
  }
  .spine-text { writing-mode: vertical-rl; color: var(--ink-light); white-space: nowrap; }
  .spine-title { display: flex; align-items: center; gap: 4px; line-height: 1; }
  .spine-title .script { font-family: "Italianno", cursive; font-size: 22px; color: var(--ember-soft); }
  .spine-title .serif { font-family: "Cormorant Garamond", serif; font-size: 16px; }
  .spine-author { font-family: "Montserrat", sans-serif; font-size: 10px; letter-spacing: 2px; text-transform: uppercase; }

  .front-cover { color: var(--ink-light); }
  .author-band {
    position: absolute; left: 0; right: 0; top: 0; height: 42px;
    background: linear-gradient(90deg, #d85e22, var(--ember) 50%, #e98a3a);
    display: flex; align-items: center; justify-content: center;
    font-family: "Montserrat", sans-serif; font-weight: 600; font-size: 15px; letter-spacing: 3px; color: #fff;
  }
  .title-block { position: absolute; left: 34px; right: 20px; top: 330px; }
  .title-block h1 { font-weight: normal; }
  .title-script { font-family: "Italianno", cursive; font-size: 54px; line-height: .8; color: var(--ember-soft); }
  .title-main { font-family: "Cormorant Garamond", serif; font-weight: 600; font-size: 44px; line-height: 1; color: var(--ink-light); }
  .subtitle { margin-top: 10px; font-family: "Open Sans", sans-serif; font-size: 11px; letter-spacing: .6px; color: var(--ember-soft); }
</style>
</head>
<body>
<main class="canvas">
  <section class="full-cover">
    <div class="sunset-art" role="img" aria-label="Soft abstract sunset glow over a dark blue night sky"></div>

    <article class="back-cover">
      <div class="back-copy">
        <p>Lantern Road Ventures: Loose Pages of a Harbor Keeper is an honest account of a business owner’s experience attempting to navigate the start-up community while also pursuing spiritual growth. Author Mirela Dunbar defines a spiritual entrepreneur as “someone who runs an enterprise with the purpose of growing love rather than material gain.” This book discusses the three dimensions of Lantern Road Ventures:</p>
        <ol>
          <li>1. The business is an integral part of the founder’s spiritual journey.</li>
          <li>2. Employees working for the spiritual enterprise, whether they know it or not, encounter this company because it's part of their spiritual path.</li>
          <li>3. The business itself has a life force of its own and its purpose is to further the kingdom of heaven on earth.</li>
        </ol>
        <p>These three dimensions happen simultaneously and work together to produce the greatest possible result. However, this can feel confusing to a founder juggling these dimensions while also trying to manage and run a business. This is not a formulaic self-help book or roadmap. Rather, it is a compilation of personal reflections that often seem at odds with the traditional world of entrepreneurship.</p>
      </div>
      <div class="author-block">
        <div class="author-photo" role="img" aria-label="Portrait photo of the author"></div>
        <p class="author-bio">Mirela Dunbar founded Calveta with the vision of ushering in a life-long education system that shifts away from standardization to one that empowers people to live their purpose. In college, Mirela interned for Open Kettle, a women’s empowerment initiative where she recognized her passion for helping people find their voice. Mirela's 20-year journey has come full circle to empowering other female CEOs who are pursuing the path of Lantern Road Ventures.</p>
      </div>
      <div class="barcode-area" aria-hidden="true"></div>
    </article>

    <aside class="spine">
      <span class="spine-text spine-title"><span class="script">Lantern Road</span><span class="serif">Ventures</span></span>
      <span class="spine-text spine-author">Mirela T. Dunbar</span>
    </aside>

    <article class="front-cover">
      <header class="author-band">MIRELA T. DUNBAR</header>
      <div class="title-block">
        <h1>
          <span class="title-script">Lantern Road</span><br>
          <span class="title-main">Ventures</span>
        </h1>
        <p class="subtitle">Loose Pages of a Harbor Keeper</p>
      </div>
    </article>
  </section>
</main>
</body>
</html>
```